Re-Design my old Business Card

We need a new business card design. The current layout is lacking good design.
We manufacture building products and also offers services (www.torvalecraft.com.au)
I've attached the old business card to show you what we don't want.
I've also attached the new logo in two styles for you to chose from.
The final design should communicate smarter building design and lifestyle, with a clean and crisp designed card.

Target Market(s)

Architects, building companies

Industry/Entity Type

Business

Contact Information for Business Card

See attached old business cards for all details to include

Font styles to use
Sans Serif

Colors
9bcb3b

Requirements
Must have
• Clean crisp look
Nice to have
• Totally up to you

```html
<!DOCTYPE html>
<html lang="en">
<head>
<meta charset="utf-8">
<title>Torvale Craft – Business Card</title>
<link href="https://fonts.googleapis.com/css2?family=Mulish:ital,wght@0,400;0,700;0,800;1,800&display=swap" rel="stylesheet">
<style>
  :root {
    --green: #9bcb3b;
    --card: #1c1c1c;
    --card-deep: #151515;
    --ink: #f2f2f2;
    --muted-tree: #2a2f24;
    --bg: #e6e4e1;
  }
  * { box-sizing: border-box; margin: 0; padding: 0; }
  html, body { width: 1200px; height: 716px; overflow: hidden; }
  body {
    background: var(--bg);
    font-family: "Mulish", "Century Gothic", sans-serif;
    display: flex; align-items: center; justify-content: center; gap: 36px;
  }
  .card {
    position: relative; width: 560px; height: 320px;
    background: var(--card); overflow: hidden;
    box-shadow: 0 6px 18px rgba(0,0,0,.25);
  }

  /* back */
  .card-back { padding: 26px 34px; text-align: center; }
  .faint-tree {
    position: absolute; left: 120px; top: 30px; width: 320px; height: 260px;
    border-radius: 48% 52% 40% 45%;
    background: radial-gradient(ellipse at center, var(--muted-tree) 0%, rgba(42,47,36,.6) 55%, rgba(28,28,28,0) 75%);
  }
  .back-content { position: relative; }
  .headline {
    color: var(--green); font-weight: 800; font-style: italic;
    font-size: 14px; line-height: 1.3; text-transform: uppercase; margin-bottom: 12px;
  }
  .pitch { color: var(--green); font-size: 13px; line-height: 1.4; }
  .pitch strong { font-weight: 800; }
  .services { list-style: none; margin: 16px 0 0 60px; text-align: left; }
  .services li {
    color: var(--ink); font-size: 14px; line-height: 1.75;
    display: flex; align-items: center; gap: 10px;
  }
  .services svg { width: 16px; height: 12px; }

  /* front */
  .card-front { padding: 28px 30px; color: var(--ink); }
  .brand { display: flex; align-items: center; gap: 10px; margin-bottom: 26px; }
  .brand-square { width: 34px; height: 34px; border: 2px solid var(--green); }
  .brand-name { color: var(--green); font-size: 24px; font-weight: 800; letter-spacing: 1px; text-transform: uppercase; }
  .person-name { color: var(--green); font-size: 16px; }
  .role, .address { font-size: 13px; line-height: 1.35; }
  .office-label { color: var(--green); font-size: 14px; margin-top: 10px; }
  .contacts { list-style: none; margin-top: 14px; font-size: 13px; line-height: 1.5; }
  .contacts li { display: flex; align-items: center; gap: 8px; }
  .contacts svg { width: 11px; height: 11px; }
  .tree-art {
    position: absolute; right: 18px; bottom: 0; width: 200px; height: 240px;
    background: var(--green);
    border-radius: 50% 46% 8% 8% / 52% 48% 6% 6%;
  }
</style>
</head>
<body>

  <section class="card card-back">
    <div class="faint-tree" role="img" aria-label="Faint tree silhouette in the background"></div>
    <div class="back-content">
      <h2 class="headline">Everyone deserves smarter, safer and healthier<br>options in building, design and lifestyle.</h2>
      <p class="pitch">If you want to live and work in environments that are<br>scientifically proven to offer improved comfort, safety,<br>health and sustainability then you will choose<br><strong>Torvale Craft.</strong></p>
      <ul class="services">
        <li><svg viewBox="0 0 16 12"><path d="M1 6l5 5 9-10" fill="none" stroke="#9bcb3b" stroke-width="3"/></svg>Energy Efficiency Consulting</li>
        <li><svg viewBox="0 0 16 12"><path d="M1 6l5 5 9-10" fill="none" stroke="#9bcb3b" stroke-width="3"/></svg>Insulation Manufacturer</li>
        <li><svg viewBox="0 0 16 12"><path d="M1 6l5 5 9-10" fill="none" stroke="#9bcb3b" stroke-width="3"/></svg>Building Science Technologies</li>
      </ul>
    </div>
  </section>

  <section class="card card-front">
    <div class="brand">
      <span class="brand-square"></span>
      <span class="brand-name">Torvale Craft</span>
    </div>
    <p class="person-name">Marcus Hale</p>
    <p class="role">Account Manager Qld /<br>Northern NSW</p>
    <p class="office-label">Head Office</p>
    <p class="address">Unit 4/27 Harlow Street<br>Kingsbrook, QLD 4188</p>
    <ul class="contacts">
      <li><svg viewBox="0 0 11 11"><rect x="2.5" y="0.5" width="6" height="10" rx="1" fill="none" stroke="#9bcb3b"/></svg>0400 217 593</li>
      <li><svg viewBox="0 0 11 11"><rect width="11" height="11" fill="#9bcb3b"/><path d="M3 2c0 4 2 6 6 7l.5-2-2-.5-.8 1C5.5 7 4.5 6 4 5l1-.8L4.5 2z" fill="#1c1c1c"/></svg>1300 642 180</li>
      <li><svg viewBox="0 0 11 11"><rect width="11" height="11" fill="#9bcb3b"/><rect x="2" y="4" width="7" height="5" fill="#1c1c1c"/><rect x="3" y="1.5" width="5" height="2.5" fill="#1c1c1c"/></svg>1300 642 181</li>
      <li><svg viewBox="0 0 11 11"><rect width="11" height="11" fill="#9bcb3b"/><path d="M1.5 3l4 3.5 4-3.5" fill="none" stroke="#1c1c1c"/></svg>marcus@torvalecraft.com.au</li>
      <li><svg viewBox="0 0 11 11"><circle cx="5.5" cy="5.5" r="5" fill="#9bcb3b"/><path d="M0.5 5.5h10M5.5 0.5c-2.5 3-2.5 7 0 10M5.5 0.5c2.5 3 2.5 7 0 10" fill="none" stroke="#1c1c1c" stroke-width=".8"/></svg>www.torvalecraft.com.au</li>
    </ul>
    <div class="tree-art" role="img" aria-label="Green tree silhouette illustration"></div>
  </section>

</body>
</html>
```